New website design for small car detailing company.

We have a small cleaning company, our main focus is car detailing but we are also expanding to home and residential cleaning and power washing.
I would like the web site to have a simple layout and SEO friendly.
I would also like to have a contact page in which clients can contact us and upload pictures of the house or car so we can provide an estimate.
A Page that shows the services we offer.

Target Market(s)

High paying clients for car detailiing and focus on residential and commercial cleaning.

Industry/Entity Type

Cleaning Service

Coding

Coded - Design and coding required

Number of Pages Required

4 page

Font styles to use
Serif

Colors

Designer to choose only greyscale colors for use in the design.

Requirements
Must have
• A home page.
Blog page for SEO
Contact page with the choice of clients to upload theirs pictures so we can provide estimates with calendar integration so they can provide their available dates for service.
A pictures to sell our services.
Nice to have
• Simple but sleek desing, I am more interested in SEO Score than heavy loads

```html
<!DOCTYPE html>
<html lang="en">
<head>
<meta charset="utf-8">
<title>Shoreline Mobile Detailing – Car Detailing, Home Cleaning &amp; Power Washing</title>
<meta name="viewport" content="width=1200">
<link rel="stylesheet" href="https://fonts.googleapis.com/css2?family=Playfair+Display:wght@600;700;800&family=Lora:ital,wght@0,400;0,500;0,600;1,400;1,600&display=swap">
<style>
:root{
  --accent:#2b2b2b;
  --accent-soft:#7a7a7a;
  --hero-accent:#c9c9c9;
  --ink:#1d1d1d;
  --text:#444;
  --muted:#8a8a8a;
  --line:#e0e0e0;
  --rule:#3a3a3a;
  --light:#f3f3f3;
  --white:#fff;
}
*{box-sizing:border-box;margin:0;padding:0}
html,body{width:1200px;height:4364px;overflow:hidden;background:var(--white)}
body{font-family:"Lora",serif;color:var(--text)}
.page{position:relative;width:1200px;height:4364px;overflow:hidden}
.abs{position:absolute}
.center{text-align:center}
.accent{color:var(--accent-soft)}

/* header */
.topbar{position:absolute;left:0;top:0;width:1200px;height:46px}
.call{position:absolute;left:690px;top:11px;display:flex;align-items:center;gap:10px;color:#fff;font-size:12px}
.call .ico{width:24px;height:24px;border-radius:50%;background:var(--accent);display:flex;align-items:center;justify-content:center}
.socials{position:absolute;display:flex;gap:6px}
.socials span{width:24px;height:24px;border-radius:50%;background:#fff;display:block}
.navband{position:absolute;left:0;top:46px;width:1200px;height:51px;background:var(--accent)}
.nav{position:absolute;top:63px;left:482px;font-size:11px;color:#fff;letter-spacing:.3px}
.nav a{color:#fff;text-decoration:none;position:absolute;white-space:nowrap}
.nav a.active::after{content:"";position:absolute;left:0;right:0;top:26px;height:3px;background:#fff}
.search{position:absolute;left:814px;top:59px;width:223px;height:25px;border:1px solid #fff;border-radius:13px;color:#fff;font-size:10px;font-style:italic;padding:5px 12px}
.search svg{position:absolute;right:9px;top:5px}
.brand{position:absolute;left:161px;top:0;width:93px;height:110px;background:#fff;border-radius:0 0 8px 8px;box-shadow:0 3px 10px rgba(0,0,0,.25);display:flex;flex-direction:column;align-items:center;justify-content:center;gap:6px;padding:8px}
.brand .mark{width:14px;height:14px;background:var(--ink)}
.brand .name{font-size:9px;font-weight:600;color:var(--ink);text-align:center;line-height:1.25;text-transform:uppercase}

/* hero */
.hero-photo{position:absolute;left:0;top:0;width:1200px;height:700px;background:linear-gradient(100deg,#3b3d40 0%,#6d7074 30%,#4c4f55 55%,#2c2e31 100%)}
.hero-title{position:absolute;left:0;width:1200px;top:226px;text-align:center;font-family:"Playfair Display",serif;font-weight:800;font-size:52px;line-height:67px;color:#fff;text-transform:uppercase}
.hero-title .accent{color:var(--hero-accent)}
.hero-sub{position:absolute;left:360px;width:480px;top:434px;text-align:center;font-style:italic;font-weight:600;font-size:11.5px;line-height:21px;color:#fff}
.btn{display:inline-flex;align-items:center;justify-content:center;background:var(--accent);color:#fff;font-family:"Lora",serif;font-weight:600;font-size:11.5px;letter-spacing:1px;border-radius:22px;text-transform:uppercase}
.hero-btn{position:absolute;left:534px;top:498px;width:132px;height:40px;box-shadow:0 0 0 3px rgba(255,255,255,.35)}
.arrow-btn{position:absolute;width:36px;height:36px;border-radius:50%;background:#fff;display:flex;align-items:center;justify-content:center}
.dot{position:absolute;width:14px;height:14px;margin-left:-7px;border-radius:50%;border:2px solid var(--rule);background:#fff}
.dot::after{content:"";position:absolute;left:3px;top:3px;width:4px;height:4px;border-radius:50%;background:var(--rule)}

.eyebrow{font-size:14px;color:var(--ink)}
.heading{font-family:"Playfair Display",serif;font-size:34px;font-weight:700;color:var(--ink);line-height:1.2}
.body-text{font-size:10px;line-height:19px;color:var(--muted)}

/* about */
.feature{position:absolute;top:983px;width:120px}
.feature .label{margin-top:22px;font-size:13px;line-height:18px;color:var(--ink)}
.photo{background:linear-gradient(135deg,#9a9ea3,#55595e)}

/* cards */
.card{position:absolute;background:#fff;box-shadow:0 2px 12px rgba(0,0,0,.08)}
.card .img{width:100%;border-bottom:4px solid var(--rule);border-radius:0 0 50% 50% / 0 0 55px 55px}
.card h3{font-weight:500;font-size:15px;color:var(--ink);text-align:center}
.card p{font-size:9.5px;line-height:19px;color:var(--muted);text-align:center}
.btn-outline{display:flex;align-items:center;justify-content:center;width:98px;height:28px;border:1px solid var(--accent);border-radius:14px;color:var(--accent);font-weight:600;font-size:10px;letter-spacing:1px;margin:0 auto}

/* testimonial */
.quote-box{position:absolute;left:300px;top:2229px;width:607px;height:208px;border:1px solid var(--line)}
.quote-text{position:absolute;left:340px;top:2292px;width:527px;text-align:center;font-size:10.5px;line-height:23px;font-style:italic;color:var(--muted)}
.sq-arrow{position:absolute;width:28px;height:28px;border:1px solid var(--line);background:#fff;display:flex;align-items:center;justify-content:center}

/* contact */
.field{position:absolute;height:44px;border:1px solid var(--line);background:#fff;font-size:9.5px;color:#555;padding:14px 12px;border-radius:3px}
.field.focus{border-color:var(--rule)}
.field svg{position:absolute}

/* blog */
.date{font-size:10px;font-weight:600;color:var(--accent-soft);letter-spacing:.8px;text-align:center}
.card h4{font-weight:400;font-size:15px;line-height:23px;color:var(--ink);text-align:center}
.more{font-size:10px;font-weight:600;color:var(--accent);letter-spacing:1px;text-align:center;display:flex;justify-content:center;align-items:center;gap:8px}

/* footer */
.foot-title{position:absolute;font-family:"Playfair Display",serif;font-size:16px;font-weight:700;color:#fff;text-align:center}
.foot-text{position:absolute;font-size:10px;line-height:18px;color:#d5d5d5;text-align:center}
.foot-nav{position:absolute;left:0;width:1200px;top:4224px;text-align:center;font-size:11px;color:#fff;word-spacing:2px}
.copyright{position:absolute;left:0;width:1200px;top:4262px;text-align:center;font-size:8.5px;color:#cfcfcf}
.copyright .muted{color:#9a9a9a}
.newsletter{position:absolute;left:663px;top:4085px;width:313px;height:42px;border-radius:21px;background:#fff;font-size:12px;color:#333;padding:12px 14px}
.newsletter .go{position:absolute;right:5px;top:5px;width:32px;height:32px;border-radius:50%;background:var(--accent);display:flex;align-items:center;justify-content:center}
</style>
</head>
<body>
<div class="page">

<header>
  <div class="hero-photo" role="img" aria-label="Detailer cleaning the interior of a car"></div>
  <div class="topbar">
    <div class="call"><span class="ico"><svg width="12" height="12" viewBox="0 0 24 24"><path fill="#fff" d="M6.6 10.8a15 15 0 0 0 6.6 6.6l2.2-2.2a1 1 0 0 1 1-.25 11 11 0 0 0 3.6.6 1 1 0 0 1 1 1V20a1 1 0 0 1-1 1A17 17 0 0 1 3 4a1 1 0 0 1 1-1h3.5a1 1 0 0 1 1 1c0 1.25.2 2.45.6 3.6a1 1 0 0 1-.25 1z"/></svg></span>Call Us Today &nbsp;:&nbsp; 123.456.7890</div>
    <div class="socials" style="left:937px;top:11px"><span></span><span></span><span></span></div>
  </div>
  <div class="navband"></div>
  <nav class="nav" aria-label="Main">
    <a class="active" href="#" style="left:0">HOME</a>
    <a href="#" style="left:59px">ABOUT</a>
    <a href="#" style="left:123px">SERVICES</a>
    <a href="#" style="left:198px">BLOG</a>
    <a href="#" style="left:254px">CONTACT</a>
  </nav>
  <div class="search">Search here...<svg width="13" height="13" viewBox="0 0 24 24"><circle cx="10" cy="10" r="7" stroke="#fff" stroke-width="2.4" fill="none"/><path d="M15 15l6 6" stroke="#fff" stroke-width="2.4"/></svg></div>
  <div class="brand"><span class="mark"></span><span class="name">Shoreline Mobile Detailing</span></div>

  <h1 class="hero-title">Best <span class="accent">Cleaning</span><br><span class="accent">Service</span> Company in<br>The <span class="accent">Town</span></h1>
  <p class="hero-sub">Lorem ipsum dolor sit amet, consectetur adipiscing elit, sed do eiusmod tempor incididunt ullamco laboris nisi ut aliquip ex ea commodo consequat.</p>
  <a class="btn hero-btn">Contact Us</a>
  <div class="arrow-btn" style="left:142px;top:316px"><svg width="10" height="10" viewBox="0 0 10 10"><path d="M6.5 1.5L3 5l3.5 3.5" stroke="#222" stroke-width="1.4" fill="none"/></svg></div>
  <div class="arrow-btn" style="left:1021px;top:316px"><svg width="10" height="10" viewBox="0 0 10 10"><path d="M3.5 1.5L7 5 3.5 8.5" stroke="#222" stroke-width="1.4" fill="none"/></svg></div>

  <svg class="abs" style="left:0;top:540px" width="1200" height="170" viewBox="0 540 1200 170">
    <path d="M0,551 L150,551 C300,720 900,720 1050,551 L1200,551 L1200,710 L0,710 Z" fill="#fff"/>
    <path d="M0,551 L150,551 C300,720 900,720 1050,551 L1200,551" fill="none" stroke="#3a3a3a" stroke-width="5"/>
  </svg>
  <div class="abs" style="left:600px;top:680px;width:1px;height:40px;background:#e0e0e0"></div>
  <div class="dot" style="left:600px;top:720px"></div>
</header>

<section aria-labelledby="why">
  <p class="eyebrow abs" style="left:163px;top:756px">About company</p>
  <h2 id="why" class="heading abs" style="left:163px;top:782px">Why <span class="accent">Choose Us</span></h2>
  <p class="body-text abs" style="left:163px;top:843px;width:400px">Lorem ipsum dolor sit amet, consectetur adipiscing elit, sed do eiusmod temporedfte incididunt ut labore et dolore magna aliqua. Ut enim ad minim veniam, quis nostrud exercitation ullamco laboris nisi ut aliquip ex ea commodo consequat. Duis aute irur dolor in reprehenderit in voluptate velit esse cillum dolore eu fugiat nulla pariatur. Excepteur sint occaecat cupidatat non proident, sunt in culpa qui officia deserunt mollit anim id est laborum.</p>

  <div class="feature" style="left:163px">
    <svg width="44" height="44" viewBox="0 0 44 44" fill="none" stroke="#2b2b2b" stroke-width="1.6"><rect x="6" y="4" width="26" height="34" rx="2"/><path d="M12 12h14M12 18h14M12 24h9"/><circle cx="32" cy="32" r="7"/><path d="M29 32l2 2 4-4"/></svg>
    <p class="label">Experience<br>Skills</p>
  </div>
  <div class="feature" style="left:302px">
    <svg width="44" height="44" viewBox="0 0 44 44" fill="none" stroke="#2b2b2b" stroke-width="1.6"><rect x="16" y="4" width="22" height="28" rx="2"/><path d="M21 12h12M21 18h12M21 24h8"/><path d="M4 40c4-8 8-12 14-12h6"/></svg>
    <p class="label">Guarantee<br>Service</p>
  </div>
  <div class="feature" style="left:437px">
    <svg width="54" height="44" viewBox="0 0 54 44" fill="none" stroke="#2b2b2b" stroke-width="1.6"><path d="M3 16l9-8 10 5 10-5 9 8-9 10-5 5-5-5-10-10z"/><path d="M22 13l-6 6M32 8l10 8M12 8L3 16"/></svg>
    <p class="label">Trusted<br>Work</p>
  </div>

  <div class="abs photo" style="left:724px;top:758px;width:315px;height:315px" role="img" aria-label="Detailer wiping down a car interior"></div>
  <div class="abs" style="left:620px;top:819px;width:195px;height:193px;background:#fff"></div>
  <div class="abs" style="left:625px;top:824px;width:185px;height:183px;background:linear-gradient(135deg,#4a4d55,#8a8c90)" role="img" aria-label="Worker washing a car"></div>
</section>

<section aria-labelledby="services">
  <svg class="abs" style="left:0;top:1270px" width="1200" height="770" viewBox="0 1270 1200 770">
    <defs><linearGradient id="svcBg" x1="0" y1="0" x2="1" y2="1"><stop offset="0" stop-color="#e6e6e6"/><stop offset="1" stop-color="#f7f7f7"/></linearGradient></defs>
    <ellipse cx="600" cy="1652" rx="760" ry="372" fill="url(#svcBg)" stroke="#3a3a3a" stroke-width="3" role="img" aria-label="Faded photo of a car being washed"/>
  </svg>
  <div class="abs" style="left:347px;top:1132px;width:501px;height:207px;background:radial-gradient(ellipse at center,#b8bcc1 0%,#8d9197 55%,rgba(141,145,151,0) 72%)" role="img" aria-label="Three workers washing a silver car"></div>

  <p class="eyebrow abs center" style="left:0;width:1200px;top:1405px">What We Offer</p>
  <h2 id="services" class="heading abs center" style="left:0;width:1200px;top:1431px">Our <span class="accent">Services</span></h2>

  <article class="card" style="left:161px;top:1505px;width:270px;height:397px">
    <div class="img" style="height:219px;background:linear-gradient(135deg,#6f6e6b,#2d2e31)" role="img" aria-label="Detailer polishing a car headlight"></div>
    <h3 style="margin-top:22px">Car Detailing</h3>
    <p style="margin:8px 18px 0">Lorem ipsum dolor sit amet, consectetur adipiscing elit, sed do eiusmod tempor incididunt ut labore et dolore magna aliqua.</p>
    <div style="margin-top:18px"><a class="btn-outline">LEARN MORE</a></div>
  </article>
  <article class="card" style="left:464px;top:1505px;width:270px;height:397px">
    <div class="img" style="height:219px;background:linear-gradient(135deg,#8a8580,#3a3d48)" role="img" aria-label="Two cleaners tidying a living room"></div>
    <h3 style="margin-top:22px">Home &amp; Residential Cleaning</h3>
    <p style="margin:8px 18px 0">Lorem ipsum dolor sit amet, consectetur adipiscing elit, sed do eiusmod tempor incididunt ut labore et dolore magna aliqua.</p>
    <div style="margin-top:18px"><a class="btn-outline">LEARN MORE</a></div>
  </article>
  <article class="card" style="left:768px;top:1505px;width:270px;height:397px">
    <div class="img" style="height:219px;background:linear-gradient(135deg,#5e625a,#9a948c)" role="img" aria-label="Worker power washing a wooden deck"></div>
    <h3 style="margin-top:22px">Power Washing</h3>
    <p style="margin:8px 18px 0">Lorem ipsum dolor sit amet, consectetur adipiscing elit, sed do eiusmod tempor incididunt ut labore et dolore magna aliqua.</p>
    <div style="margin-top:18px"><a class="btn-outline">LEARN MORE</a></div>
  </article>
  <div class="dot" style="left:600px;top:1978px"></div>
  <div class="abs" style="left:600px;top:1992px;width:1px;height:34px;background:#ccc"></div>
</section>

<section aria-labelledby="feedback">
  <p class="eyebrow abs center" style="left:0;width:1200px;top:2092px">Testimonials</p>
  <h2 id="feedback" class="heading abs center" style="left:0;width:1200px;top:2118px">Client's <span class="accent">Feedback</span></h2>
  <div class="quote-box"></div>
  <div class="abs" style="left:536px;top:2223px;width:124px;height:12px;background:#fff"></div>
  <div class="abs" style="left:538px;top:2224px;width:6px;height:6px;border-radius:50%;background:#ccc"></div>
  <div class="abs" style="left:657px;top:2224px;width:6px;height:6px;border-radius:50%;background:#ccc"></div>
  <div class="abs" style="left:561px;top:2190px;width:74px;height:74px;border-radius:50%;border:3px solid var(--rule);background:#fff;padding:3px">
    <div style="width:100%;height:100%;border-radius:50%;background:linear-gradient(135deg,#8a8d90,#44474a)" role="img" aria-label="Client portrait"></div>
  </div>
  <p class="quote-text">"Lorem ipsum dolor sit amet, consectetur adipiscing elit, sed do eiusmod temporedfte incididunt ut labore et dolore magna aliqua. Ut enim ad minim veniam, quis nostrud exercitation ullamco laboris nisi ut aliquip ex ea commodo consequat. Duis aute irur dolor in reprehenderit in voluptate velit esse cillum dolore eu fugiat nulla pariatur. Excepteur sint occaecat cupidatat non proident."</p>
  <div class="sq-arrow" style="left:285px;top:2319px"><svg width="8" height="8" viewBox="0 0 10 10"><path d="M6.5 1.5L3 5l3.5 3.5" stroke="#999" stroke-width="1.2" fill="none"/></svg></div>
  <div class="sq-arrow" style="left:893px;top:2319px"><svg width="8" height="8" viewBox="0 0 10 10"><path d="M3.5 1.5L7 5 3.5 8.5" stroke="#999" stroke-width="1.2" fill="none"/></svg></div>
  <div class="abs" style="left:578px;top:2415px;width:42px;height:42px;border-radius:50%;background:var(--accent);display:flex;align-items:center;justify-content:center">
    <svg width="22" height="18" viewBox="0 0 22 18"><path fill="#fff" d="M0 18V10C0 4 3 1 8 0l1 2C6 3 5 5 5 8h4v10zM13 18V10c0-6 3-9 8-10l1 2c-3 1-4 3-4 6h4v10z"/></svg>
  </div>
  <p class="abs center" style="left:0;width:1200px;top:2482px;font-size:13px;color:var(--ink)">-&nbsp; Client's Name</p>
</section>

<section aria-labelledby="contact">
  <svg class="abs" style="left:0;top:2570px" width="1200" height="600" viewBox="0 2570 1200 600">
    <defs><linearGradient id="ctBg" x1="0" y1="0" x2="1" y2="1"><stop offset="0" stop-color="#e4e4e4"/><stop offset="1" stop-color="#f6f6f6"/></linearGradient></defs>
    <ellipse cx="600" cy="2866" rx="849" ry="290" fill="url(#ctBg)" stroke="#3a3a3a" stroke-width="3" role="img" aria-label="Faded photo of a detailer at work"/>
  </svg>
  <div class="dot" style="left:600px;top:2612px"></div>
  <div class="dot" style="left:600px;top:3107px"></div>
  <div class="abs" style="left:600px;top:3121px;width:1px;height:30px;background:#ccc"></div>
  <p class="eyebrow abs center" style="left:390px;width:400px;top:2663px">Free Estimate</p>
  <h2 id="contact" class="heading abs center" style="left:390px;width:400px;top:2689px">Contact <span class="accent">Us</span></h2>
  <div class="abs" style="left:68px;top:2780px;width:500px;height:254px;background:radial-gradient(ellipse at center,#c9ced4 0%,#9ba3ad 45%,rgba(155,163,173,0) 70%)" role="img" aria-label="White sports car splashed with water"></div>

  <form aria-label="Free estimate">
    <div class="field focus" style="left:663px;top:2761px;width:374px">Name :</div>
    <div class="field" style="left:663px;top:2814px;width:183px">Email :</div>
    <div class="field" style="left:856px;top:2814px;width:181px">Phone :</div>
    <div class="field" style="left:663px;top:2866px;width:183px">Select Service :<svg style="right:12px;top:18px" width="10" height="6" viewBox="0 0 10 6"><path d="M1 1l4 4 4-4" stroke="#555" fill="none"/></svg></div>
    <div class="field" style="left:856px;top:2866px;width:181px">Available Dates :<svg style="right:11px;top:14px" width="14" height="14" viewBox="0 0 14 14" fill="none" stroke="#555" stroke-width="1.1"><rect x="1" y="2.5" width="12" height="10.5" rx="1"/><path d="M1 5.5h12M4 1v3M10 1v3M4 8h1.5M7 8h1.5M10 8h1M4 10.5h1.5M7 10.5h1.5"/></svg></div>
    <div class="field" style="left:663px;top:2919px;width:374px">Attached Picture :<svg style="right:10px;top:13px" width="14" height="16" viewBox="0 0 14 16"><path d="M11 7l-5 5a2.5 2.5 0 0 1-3.5-3.5L8 3a1.6 1.6 0 0 1 2.3 2.3L5 10.5" stroke="#666" fill="none" stroke-width="1.2"/></svg></div>
    <div class="field" style="left:663px;top:2971px;width:374px">Message :</div>
    <a class="btn abs" style="left:663px;top:3024px;width:166px;height:44px">Get Free Estimate</a>
  </form>
</section>

<section aria-labelledby="blog">
  <p class="eyebrow abs center" style="left:0;width:1200px;top:3217px">Blog &amp; Articals</p>
  <h2 id="blog" class="heading abs center" style="left:0;width:1200px;top:3243px">Latest <span class="accent">Blog</span></h2>

  <article class="card" style="left:161px;top:3324px;width:270px;height:413px">
    <div class="img" style="height:185px;background:linear-gradient(135deg,#5a5f6a,#2a2b2d)" role="img" aria-label="Gloved hand cleaning a dashboard"></div>
    <p class="date" style="margin-top:32px">31 AUGUST 2020</p>
    <h4 style="margin-top:8px">Lorem ipsum dolor sit amet,<br>consectetur adipiscing.</h4>
    <p style="margin:8px 18px 0">Lorem ipsum dolor sit amet, consectetur adipiscing elit, eiusmod tempor incididunt ut labore et dolore magna aliqua.</p>
    <p class="more" style="margin-top:14px">LEARN MORE <svg width="18" height="8" viewBox="0 0 18 8"><path d="M0 4h16M13 1l3 3-3 3" stroke="#2b2b2b" fill="none"/></svg></p>
  </article>
  <article class="card" style="left:464px;top:3324px;width:270px;height:413px">
    <div class="img" style="height:185px;background:linear-gradient(135deg,#5e6168,#2a2c33)" role="img" aria-label="Detailer cleaning a car wheel"></div>
    <p class="date" style="margin-top:32px">31 AUGUST 2020</p>
    <h4 style="margin-top:8px">Lorem ipsum dolor sit amet,<br>consectetur adipiscing.</h4>
    <p style="margin:8px 18px 0">Lorem ipsum dolor sit amet, consectetur adipiscing elit, eiusmod tempor incididunt ut labore et dolore magna aliqua.</p>
    <p class="more" style="margin-top:14px">LEARN MORE <svg width="18" height="8" viewBox="0 0 18 8"><path d="M0 4h16M13 1l3 3-3 3" stroke="#2b2b2b" fill="none"/></svg></p>
  </article>
  <article class="card" style="left:768px;top:3324px;width:270px;height:413px">
    <div class="img" style="height:185px;background:linear-gradient(135deg,#7d8085,#34373c)" role="img" aria-label="Man pressure washing a car"></div>
    <p class="date" style="margin-top:32px">31 AUGUST 2020</p>
    <h4 style="margin-top:8px">Lorem ipsum dolor sit amet,<br>consectetur adipiscing.</h4>
    <p style="margin:8px 18px 0">Lorem ipsum dolor sit amet, consectetur adipiscing elit, eiusmod tempor incididunt ut labore et dolore magna aliqua.</p>
    <p class="more" style="margin-top:14px">LEARN MORE <svg width="18" height="8" viewBox="0 0 18 8"><path d="M0 4h16M13 1l3 3-3 3" stroke="#2b2b2b" fill="none"/></svg></p>
  </article>
</section>

<footer>
  <svg class="abs" style="left:0;top:3790px" width="1200" height="574" viewBox="0 3790 1200 574" role="img" aria-label="Dark photo of a detailer at work">
    <defs><linearGradient id="ftBg" x1="0" y1="0" x2="1" y2="1"><stop offset="0" stop-color="#2f3033"/><stop offset="1" stop-color="#1c1d1f"/></linearGradient></defs>
    <path d="M0,3935 L160,3935 C300,3762 900,3762 1040,3935 L1200,3935 L1200,4364 L0,4364 Z" fill="url(#ftBg)"/>
    <path d="M0,3935 L160,3935 C300,3762 900,3762 1040,3935 L1200,3935" fill="none" stroke="#8a8a8a" stroke-width="5"/>
  </svg>
  <div class="brand" style="left:556px;top:3813px;width:88px;height:124px"><span class="mark"></span><span class="name">Shoreline Mobile Detailing</span></div>
  <div class="abs" style="left:599px;top:3955px;width:1px;height:235px;background:rgba(255,255,255,.25)"></div>

  <h3 class="foot-title" style="left:180px;width:400px;top:3974px">Get In Touch</h3>
  <p class="foot-text" style="left:180px;width:400px;top:4017px">123 - Address, State name, Street name,<br>City Name, Zipcode</p>
  <p class="foot-text" style="left:180px;width:400px;top:4074px;font-size:11px;color:#fff">Phone : 123.456.7890</p>
  <p class="foot-text" style="left:180px;width:400px;top:4104px;font-size:11px;color:#fff">Email : hello@shorelinedetail.com</p>

  <h3 class="foot-title" style="left:619px;width:400px;top:3974px">Subcribe Newsletter</h3>
  <p class="foot-text" style="left:669px;width:300px;top:4017px">Lorem ipsum dolor sit amet, consectetur adipiscing elit, sed do eiusmod tempor incididunt.</p>
  <div class="newsletter">Enter Email<span class="go"><svg width="14" height="14" viewBox="0 0 24 24"><path fill="#fff" d="M2 21l21-9L2 3v7l15 2-15 2z"/></svg></span></div>

  <nav class="foot-nav" aria-label="Footer">Home &nbsp;| &nbsp;About &nbsp;| &nbsp;Services &nbsp;| &nbsp;Blog &nbsp;| &nbsp;Contact</nav>
  <p class="copyright">Copyright © SHORELINE MOBILE DETAILING CLEANING COMPANY - 2020 . <span class="muted">All Right Reserved.</span></p>
  <div class="socials" style="left:547px;top:4293px;gap:9px"><span style="width:28px;height:28px"></span><span style="width:28px;height:28px"></span><span style="width:28px;height:28px"></span></div>
</footer>

</div>
</body>
</html>
```